Torvin Home care non-medical home care brochure

Develop a eye catching non-medical Homecare brochure, detailing services we provide. Services
Personal Care Attendants
Extended Care Attendants
Non-Medical Transportation
We accept
Calvora Wellcare
Long Term Care Insurance Plans
Private Pay

HELP WITH:
Eating
Bathing
Dressing
Grooming
Moving from one surface to another
Walking or using a wheelchair
Toileting
Changing positions in bed
OTHER SERVICES:
Light housekeeping
Preparing and storing meals
Shopping
Laundry
Reminders about taking medicines
Help with medical appointments
Help finding transportation for appts.

Target Market(s)

Seniors and individuals needing non-medical assistance.

Industry/Entity Type

Health Care

Font styles to use
Sans Serif

Requirements
Must have
• Details regarding services, tri-fold design
Nice to have
• Logo, details detailng services
Should not have
• n/a

```html
<!DOCTYPE html>
<html lang="en">
<head>
<meta charset="utf-8">
<title>Torvin Homecare – Tri-fold Brochure</title>
<link rel="stylesheet" href="https://fonts.googleapis.com/css2?family=Montserrat:wght@400;600;700;800&display=swap">
<style>
  :root {
    --navy: #2b2d4e;
    --navy-deep: #24263f;
    --red: #e0191f;
    --paper: #f1f1f1;
    --paper-edge: #dcdcdc;
    --ink: #2b2d4e;
    --muted: #55576e;
    --cover-title: #e4e4e8;
    --backdrop: #ebe8e3;
    --photo-warm: #c9b8a6;
    --photo-green: #a9b98f;
    --photo-blue: #8fa3c2;
  }
  * { margin: 0; padding: 0; box-sizing: border-box; }
  html, body { width: 1200px; height: 900px; overflow: hidden; }
  body {
    background: var(--backdrop);
    font-family: "Montserrat", Arial, sans-serif;
    color: var(--ink);
    position: relative;
  }
  .spread {
    position: absolute;
    top: 227px;
    width: 576px;
    height: 446px;
    display: flex;
    overflow: hidden;
    box-shadow: 0 6px 18px rgba(0,0,0,.18);
  }
  .spread--outside { left: 16px; }
  .spread--inside { left: 608px; }
  .panel { position: relative; width: 192px; height: 446px; flex: none; overflow: hidden; }
  .panel--light { background: linear-gradient(90deg, var(--paper-edge), var(--paper) 40%, #fafafa); }
  .panel--navy { background: var(--navy); color: #fff; }

  .section-title {
    font-weight: 800; font-size: 10px; color: var(--red);
    letter-spacing: .2px; text-transform: uppercase;
  }
  .tick-list { list-style: none; }
  .tick-list li {
    position: relative; padding-left: 14px;
    font-size: 7.6px; font-weight: 600; line-height: 1.45;
    margin-top: 4px;
  }
  .tick-list li::before {
    content: "✓"; position: absolute; left: 0; top: 0;
    font-size: 7px; color: currentColor; opacity: .8;
  }
  .diamond-list { list-style: none; margin-top: 6px; }
  .diamond-list li {
    position: relative; padding-left: 13px;
    font-size: 7.8px; font-weight: 700; line-height: 1.35;
    margin-bottom: 7px;
  }
  .diamond-list li::before {
    content: ""; position: absolute; left: 1px; top: 3px;
    width: 4px; height: 4px; background: var(--red); transform: rotate(45deg);
  }

  /* outside: other services */
  .other-services { position: absolute; left: 26px; top: 38px; width: 150px; }
  .other-services .tick-list { margin-top: 4px; }
  .photo-fill { position: absolute; }
  .other-services-photo {
    left: 0; top: 252px; width: 192px; height: 194px;
    background: linear-gradient(135deg, #e9ecef 0%, var(--photo-blue) 35%, #d9d2c8 60%, var(--photo-warm) 100%);
  }
  .corner-triangle { position: absolute; left: 0; bottom: 0; }

  /* outside: back panel */
  .brand-name {
    font-weight: 800; color: #fff; text-transform: uppercase;
    display: flex; align-items: center; gap: 7px; justify-content: center;
  }
  .brand-name__square { width: 9px; height: 9px; background: var(--red); flex: none; }
  .back-brand { position: absolute; left: 0; right: 0; top: 200px; font-size: 15px; letter-spacing: .5px; }
  .contact { position: absolute; left: 30px; top: 368px; list-style: none; }
  .contact li {
    display: flex; gap: 7px; align-items: flex-start;
    font-size: 6.4px; line-height: 1.35; color: #d8d9e4; margin-bottom: 5px;
  }
  .contact svg { flex: none; margin-top: 1px; }

  /* outside: cover */
  .panel--cover { background: var(--navy); }
  .cover-top { position: absolute; left: 0; top: 0; width: 192px; height: 60px; background: linear-gradient(#f4f4f4, #e2e2e2); }
  .cover-brand {
    position: absolute; left: 0; right: 0; top: 22px;
    font-size: 10px; color: var(--navy); letter-spacing: .4px;
  }
  .cover-art { position: absolute; left: 0; top: 0; }
  .cover-title {
    position: absolute; left: 22px; top: 352px;
    font-weight: 800; font-size: 21px; line-height: 1.15; color: var(--cover-title);
  }
  .cover-web {
    position: absolute; left: 22px; top: 419px;
    font-weight: 700; font-size: 8px; color: var(--red);
  }

  /* inside: intro */
  .intro { position: absolute; left: 26px; top: 26px; width: 145px; }
  .intro p { font-size: 6.5px; line-height: 1.32; color: var(--muted); margin-bottom: 6px; }
  .intro-photo {
    left: 0; top: 200px; width: 384px; height: 246px;
    background: linear-gradient(120deg, #e4e6ea 0%, #d7cbbd 35%, var(--photo-warm) 55%, #eceae6 85%);
  }

  /* inside: services */
  .services { position: absolute; left: 24px; top: 36px; width: 160px; z-index: 2; }
  .services .section-title + .diamond-list { margin-bottom: 12px; }

  /* inside: help with */
  .mosaic { position: absolute; left: 0; top: 0; }
  .help-with { position: absolute; left: 34px; top: 244px; width: 150px; }
  .help-with .section-title { color: #fff; font-size: 9px; }
  .help-with .tick-list li { color: #eef0f6; margin-top: 5px; }
</style>
</head>
<body>

<!-- Outside spread -->
<section class="spread spread--outside" aria-label="Brochure outside">
  <div class="panel panel--light">
    <div class="other-services">
      <h3 class="section-title">Other services:</h3>
      <ul class="tick-list">
        <li>Light housekeeping</li>
        <li>Preparing and storing meals</li>
        <li>Shopping</li>
        <li>Laundry</li>
        <li>Reminders about taking medicines</li>
        <li>Help with medical appointments</li>
        <li>Help finding transportation for appts.</li>
      </ul>
    </div>
    <div class="photo-fill other-services-photo" role="img" aria-label="Photo: caregiver in blue scrubs serving a meal to an elderly man at a table"></div>
    <svg class="corner-triangle" width="42" height="42" viewBox="0 0 42 42"><polygon points="0,0 42,42 0,42" fill="var(--red)"/></svg>
  </div>

  <div class="panel panel--navy">
    <div class="brand-name back-brand"><span class="brand-name__square"></span>Torvin Homecare</div>
    <ul class="contact">
      <li>
        <svg width="7" height="8" viewBox="0 0 10 12"><path d="M5 0a4 4 0 0 1 4 4c0 3-4 8-4 8S1 7 1 4a4 4 0 0 1 4-4z" fill="#d8d9e4"/><circle cx="5" cy="4" r="1.5" fill="var(--navy)"/></svg>
        <span>48 Birchwell Rd #2,<br>Alder, ON, K2M 4R7</span>
      </li>
      <li>
        <svg width="7" height="7" viewBox="0 0 10 10"><circle cx="5" cy="5" r="5" fill="#d8d9e4"/><path d="M2.5 3.5h5v3h-5z" fill="none" stroke="var(--navy)" stroke-width=".8"/><path d="M2.5 3.5 5 5.3l2.5-1.8" fill="none" stroke="var(--navy)" stroke-width=".8"/></svg>
        <span>sales@torvinhomecare.com</span>
      </li>
      <li>
        <svg width="7" height="7" viewBox="0 0 10 10"><circle cx="5" cy="5" r="5" fill="#d8d9e4"/><path d="M3.3 2.6l1 1-.6.8a4 4 0 0 0 1.9 1.9l.8-.6 1 1-.7.8C5 7.3 2.7 5 2.6 3.3z" fill="var(--navy)"/></svg>
        <span>(000) 555-0142</span>
      </li>
    </ul>
  </div>

  <div class="panel panel--cover">
    <div class="cover-top"></div>
    <svg class="cover-art" width="192" height="446" viewBox="0 0 192 446">
      <defs>
        <linearGradient id="coverPhotoTone" x1="0" y1="0" x2="1" y2="1">
          <stop offset="0" stop-color="var(--photo-green)"/>
          <stop offset=".45" stop-color="var(--photo-warm)"/>
          <stop offset=".75" stop-color="var(--photo-blue)"/>
          <stop offset="1" stop-color="#d6d6d6"/>
        </linearGradient>
      </defs>
      <polygon points="0,248 96,340 192,248 192,262 96,356 0,262" fill="#ffffff"/>
      <polygon points="0,60 192,60 192,238 96,330 0,238" fill="url(#coverPhotoTone)" role="img" aria-label="Photo: smiling caregiver embracing a smiling elderly man outdoors"/>
    </svg>
    <div class="brand-name cover-brand"><span class="brand-name__square"></span>Torvin Homecare</div>
    <h1 class="cover-title">Torvin<br>Homecare</h1>
    <div class="cover-web">www.torvinhomecare.com</div>
  </div>
</section>

<!-- Inside spread -->
<section class="spread spread--inside" aria-label="Brochure inside">
  <div class="panel panel--light" style="overflow:visible; z-index:1;">
    <div class="intro">
      <p>Lorem ipsum dolor sit amet, consectetur adipiscing elit. Nunc semper quis arcu nec tincidunt. Cras in rhoncus risus. Vestibulum tincidunt molestie purus non egestas. Integer iaculis lobortis.</p>
      <p>Praesent blandit sem a odio laoreet, quis molestie dolor faucibus. Quisque non consectetur lacus. Sed condimentum rutrum arcu, a rutrum urna mollis sed. Ut commodo varius erat, at interdum velit ornare ut. Aliquam convallis nulla ut mattis efficitur.</p>
      <p>Aenean sodales erat in libero pulvinar, sed semper dui ultrices. Praesent vehicula quam vel ligula rutrum porttitor.</p>
    </div>
    <div class="photo-fill intro-photo" role="img" aria-label="Photo: happy senior couple hugging in a bright living room"></div>
    <svg class="corner-triangle" width="38" height="52" viewBox="0 0 38 52"><polygon points="0,0 38,52 0,52" fill="var(--red)"/></svg>
  </div>

  <div class="panel panel--light" style="background:linear-gradient(90deg,#f7f7f7,#e9e9e9);">
    <div class="services">
      <h3 class="section-title">Services</h3>
      <ul class="diamond-list">
        <li>Personal Care Attendants</li>
        <li>Extended Care Attendants</li>
        <li>Non-Medical Transportation</li>
      </ul>
      <h3 class="section-title">We accept</h3>
      <ul class="diamond-list">
        <li>Calvora Wellcare</li>
        <li>Long Term Care Insurance Plans</li>
        <li>Private Pay</li>
      </ul>
    </div>
  </div>

  <div class="panel panel--navy">
    <svg class="mosaic" width="192" height="446" viewBox="0 0 192 446">
      <defs>
        <linearGradient id="mosaicToneA" x1="0" y1="0" x2="1" y2="1">
          <stop offset="0" stop-color="var(--photo-blue)"/><stop offset="1" stop-color="#e8d8dc"/>
        </linearGradient>
        <linearGradient id="mosaicToneB" x1="0" y1="0" x2="1" y2="1">
          <stop offset="0" stop-color="#c8d4de"/><stop offset="1" stop-color="#efeff1"/>
        </linearGradient>
        <linearGradient id="mosaicToneC" x1="0" y1="0" x2="1" y2="1">
          <stop offset="0" stop-color="#c99a45"/><stop offset=".5" stop-color="#8c6e4a"/><stop offset="1" stop-color="var(--photo-blue)"/>
        </linearGradient>
      </defs>
      <polygon points="18,0 62,0 40,22" fill="var(--red)"/>
      <polygon points="192,60 192,170 140,118" fill="var(--red)"/>
      <polygon points="0,150 0,262 56,206" fill="var(--red)"/>
      <polygon points="124,-26 188,38 124,102 60,38" fill="url(#mosaicToneA)" stroke="#fff" stroke-width="3" role="img" aria-label="Photo: nurse assisting an elderly woman in bed"/>
      <polygon points="61,48 124,111 61,174 -2,111" fill="url(#mosaicToneB)" stroke="#fff" stroke-width="3" role="img" aria-label="Photo: caregiver tending to a resting senior man"/>
      <polygon points="124,110 188,174 124,238 60,174" fill="url(#mosaicToneC)" stroke="#fff" stroke-width="3" role="img" aria-label="Photo: caregiver walking with a senior man using a walker outdoors in autumn"/>
      <line x1="124" y1="238" x2="192" y2="306" stroke="#fff" stroke-width="3"/>
    </svg>
    <div class="help-with">
      <h3 class="section-title">Help with :</h3>
      <ul class="tick-list">
        <li>Eating</li>
        <li>Bathing</li>
        <li>Dressing</li>
        <li>Grooming</li>
        <li>Moving from one surface to another</li>
        <li>Walking or using a wheelchair</li>
        <li>Toileting</li>
        <li>Changing positions in bed</li>
      </ul>
    </div>
  </div>
</section>

</body>
</html>
```